Folder & Business Card for Automation Company
Brightwell Torque Mfr.
Folder & Business Card for Automation Company - Manufacturing
Creative Brief
Professional
Darren Okafor
Vice President
4817 Halvern Road Merriam, KS 66209
do@brightwelltorquemfr.example
www.brightwelltorquemfr.example
Along with a business card we are looking for a design for the front cover of a folder to be used for sales literature. The cover should also include our logo.

```html
<!DOCTYPE html>
<html lang="en">
<head>
<meta charset="utf-8">
<title>Brightwell Torque Mfr. — Business Card</title>
<link rel="stylesheet" href="https://fonts.googleapis.com/css2?family=Cormorant+SC:wght@500;700&display=swap">
<style>
  :root {
    --backdrop: #e9e6e2;
    --card-white: #ffffff;
    --charcoal: #2f2f31;
    --charcoal-deep: #1f1f21;
    --accent-red: #d31f26;
    --ink-light: #e6e6e6;
    --ink-muted: #bdbdbd;
    --ink-dark: #1c1c1c;
  }
  html, body {
    margin: 0;
    padding: 0;
    width: 1200px;
    height: 914px;
    overflow: hidden;
    background: var(--backdrop);
  }
  .canvas {
    position: relative;
    width: 1200px;
    height: 914px;
  }
  .business-card {
    position: absolute;
    left: 75px;
    top: 157px;
    width: 1050px;
    height: 600px;
    background: var(--card-white);
    box-shadow: 0 10px 30px rgba(0,0,0,0.18);
    overflow: hidden;
    font-family: "Cormorant SC", Georgia, serif;
  }
  .card-shapes {
    position: absolute;
    inset: 0;
  }
  .identity {
    position: absolute;
    left: 110px;
    top: 38px;
    color: var(--ink-light);
  }
  .identity .person-name {
    font-size: 32px;
    font-weight: 500;
    letter-spacing: 0.5px;
    line-height: 1;
    margin: 0;
  }
  .identity .person-title {
    font-size: 22px;
    font-weight: 500;
    color: var(--ink-muted);
    margin: 4px 0 0;
  }
  .contact-list {
    position: absolute;
    left: 44px;
    top: 300px;
    margin: 0;
    padding: 0;
    list-style: none;
    color: var(--ink-light);
    font-size: 17px;
    font-weight: 500;
    line-height: 1.15;
  }
  .contact-list li {
    display: flex;
    align-items: flex-start;
    gap: 10px;
    margin-bottom: 4px;
  }
  .contact-icon {
    flex: 0 0 auto;
    width: 16px;
    height: 16px;
    margin-top: 2px;
  }
  .brand-lockup {
    position: absolute;
    left: 600px;
    top: 230px;
    display: flex;
    align-items: center;
    gap: 16px;
  }
  .brand-mark {
    flex: 0 0 auto;
    width: 22px;
    height: 22px;
    border-radius: 50%;
    background: var(--accent-red);
  }
  .brand-name {
    font-size: 50px;
    font-weight: 700;
    color: var(--ink-dark);
    letter-spacing: 0.5px;
    line-height: 0.95;
  }
</style>
</head>
<body>
<main class="canvas">
  <article class="business-card">
    <svg class="card-shapes" width="1050" height="600" viewBox="0 0 1050 600" aria-hidden="true">
      <defs>
        <radialGradient id="panel-shade" cx="0.35" cy="0.4" r="0.8">
          <stop offset="0" stop-color="#333335"/>
          <stop offset="1" stop-color="#1f1f21"/>
        </radialGradient>
      </defs>
      <path class="accent-arc" d="M490 0 Q535 330 365 600 L387 600 Q562 330 518 0 Z" fill="var(--accent-red)"/>
      <path class="dark-panel" d="M0 0 L470 0 Q515 330 345 600 L0 600 Z" fill="url(#panel-shade)"/>
    </svg>

    <header class="identity">
      <h1 class="person-name">Darren Okafor</h1>
      <p class="person-title">Vice President</p>
    </header>

    <ul class="contact-list">
      <li>
        <svg class="contact-icon" viewBox="0 0 18 18"><circle cx="9" cy="9" r="9" fill="var(--ink-light)"/><path d="M9 4 L14 8.5 H12.5 V13 H5.5 V8.5 H4 Z" fill="var(--charcoal)"/></svg>
        <span>4817 Halvern Road<br>Merriam, KS 66209</span>
      </li>
      <li>
        <svg class="contact-icon" viewBox="0 0 18 18"><circle cx="9" cy="9" r="9" fill="var(--ink-light)"/><path d="M6 4.5 L8 6.5 L7 8 Q8 10 10 11 L11.5 10 L13.5 12 L12 13.5 Q7.5 13 4.5 6 Z" fill="var(--charcoal)"/></svg>
        <span>913-555-0147</span>
      </li>
      <li>
        <svg class="contact-icon" viewBox="0 0 18 18"><circle cx="9" cy="9" r="9" fill="var(--ink-light)"/><rect x="5" y="7" width="8" height="5" fill="var(--charcoal)"/><rect x="6.5" y="4.5" width="5" height="2.5" fill="var(--charcoal)"/></svg>
        <span>913-555-0182</span>
      </li>
      <li>
        <svg class="contact-icon" viewBox="0 0 18 18"><circle cx="9" cy="9" r="9" fill="var(--ink-light)"/><rect x="4.5" y="5.5" width="9" height="7" fill="var(--charcoal)"/><path d="M4.5 5.5 L9 9.5 L13.5 5.5" stroke="var(--ink-light)" fill="none"/></svg>
        <span>do@brightwelltorquemfr.example</span>
      </li>
      <li>
        <svg class="contact-icon" viewBox="0 0 18 18"><circle cx="9" cy="9" r="9" fill="var(--ink-light)"/><circle cx="9" cy="9" r="4.5" fill="none" stroke="var(--charcoal)" stroke-width="1.3"/><path d="M4.5 9 H13.5 M9 4.5 V13.5" stroke="var(--charcoal)" stroke-width="1.1"/></svg>
        <span>www.brightwelltorquemfr.example</span>
      </li>
    </ul>

    <div class="brand-lockup">
      <span class="brand-mark"></span>
      <span class="brand-name">Brightwell<br>Torque Mfr.</span>
    </div>
  </article>
</main>
</body>
</html>
```